Company or website name
- www.brambletonhiregroup.example
- Links to the website
- Brambleton Hire Group
- Describe your company and organization and target audience
- We are a full service executive recruiting and staffing company. We work within all vertical markets within the US.
- The design should have the following
- Please ensure to include colors of the logo but feel free to include other colors as well to enhance the brochure. I'm looking for a single 8.5 x 11 inch brochure with front and back. The back will have more specific information while the front will be more a space for photos and general information on our company.
- Other Facts

```html
<!DOCTYPE html>
<html lang="en">
<head>
<meta charset="utf-8">
<title>Brambleton Hire Group – Brochure Spread</title>
<link rel="stylesheet" href="https://fonts.googleapis.com/css2?family=Open+Sans:wght@400;600;700&display=swap">
<style>
:root{
  --brand-blue:#1f4f9e;
  --brand-blue-dark:#163c7c;
  --brand-blue-light:#2f67bd;
  --accent-red:#e01e4f;
  --ink:#3d3d3d;
  --heading-blue:#1f4f9e;
  --paper:#ffffff;
  --backdrop:#e9e9e9;
  --photo-dark:#1b1d22;
  --photo-mid:#4a4e57;
}
*{box-sizing:border-box;margin:0;padding:0}
html,body{width:1200px;height:848px;overflow:hidden;background:var(--backdrop)}
body{font-family:"Open Sans",Arial,sans-serif;color:var(--ink)}
.spread{position:absolute;left:0;top:0;width:1200px;height:848px;display:flex;background:var(--paper)}
.page{position:relative;width:600px;height:848px;overflow:hidden}
.page--left{border-right:1px solid #d6d6d6}

.about{height:410px;background:linear-gradient(160deg,var(--brand-blue-light),var(--brand-blue) 45%,var(--brand-blue-dark));color:#fff;padding:34px 40px 0 40px}
.pill{display:inline-block;background:var(--accent-red);color:#fff;font-weight:700;font-size:13px;padding:3px 22px 3px 14px;border-radius:0 12px 12px 0;margin-bottom:8px}
.about h3{font-size:13px;font-weight:700;margin:8px 0 3px}
.about p{font-size:9.2px;line-height:12.5px;margin-bottom:5px;color:#e8eefa}

.seekers{padding:26px 40px 0 40px}
.seekers .intro{font-size:9.5px;line-height:13px;margin-bottom:12px}
.seekers .intro em{color:var(--heading-blue);font-style:italic}
.columns{display:flex;gap:22px}
.columns .col{flex:1}
.col h4{color:var(--heading-blue);font-size:11px;font-weight:700;margin-bottom:6px}
.col p{font-size:9.3px;line-height:12.8px;margin-bottom:10px}

.employers{padding:30px 40px 0 40px;height:440px}
.employers .lead{font-size:12.5px;font-weight:700;color:#222;margin:2px 0 6px}
.employers h4{color:var(--heading-blue);font-size:10.5px;font-weight:700;margin:7px 0 2px}
.employers p{font-size:9px;line-height:12px;margin-bottom:4px}
.team-photo{position:absolute;left:0;bottom:0;width:600px;height:402px;background:radial-gradient(ellipse at 55% 30%,var(--photo-mid),var(--photo-dark) 70%)}
</style>
</head>
<body>
<main class="spread">
  <section class="page page--left">
    <div class="about">
      <span class="pill">About Brambleton</span>
      <h3>Why Choose Our Services</h3>
      <p>Our expertise in recruiting and staffing in administrative, financial, legal, human resources, information technology, healthcare and property management helps you meet all competitive challenges. Our clients tell us we contribute to their success by working under the highest ethical standard, providing exceptional talent and combining innovative solutions with outstanding customer service.</p>
      <p>What sets us apart is our single-minded focus on making customer satisfaction our top priority. Finding the right candidate is just the start of our partnership with you.</p>
      <h3>Our Process</h3>
      <p>We maintain an on-going database of over 100,000 client relationships from the industries that we serve. The depth and breadth of our candidate pool gives us the contacts, knowledge and relationships to close the candidate. On-going relationship building and candidate research are at the core of our business.</p>
      <p>While we draw on our priority database of candidates, we will also source new candidates specifically for your search in order to ensure that we get the best match possible for your needs. Our candidates undergo an intense screening process. In addition to meeting with the candidate, we interview previous supervisors, peers, subordinates and customers. We provide this information to our clients on our thorough Candidate Evaluation Report.</p>
      <h3>Our Goal</h3>
      <p>Our goal is to build the long-term partnerships with both corporate clients and candidate talent that allow us to provide the best hiring solutions in the most expedient manner. Our expert recruiters provide the individual attention that will get you the result that you are looking for in the shortest amount of time possible.</p>
      <p>Our focused team of recruiters and search specialists know that they are always looking out for number one – the client. Internally we are in constant communication with each other in order to leverage the expertise of the entire team. Throughout the process we provide status reports to our clients and candidates.</p>
    </div>
    <div class="seekers">
      <span class="pill">Job Seekers</span>
      <p class="intro">At Brambleton Hire Group, we understand where you are coming from, and can help you get to where you want to go. Our specialized recruiters know your industry and have the capability to expand your options. If you are looking for a <em>smart, driven, supportive, and honest recruiter</em>, then you are looking for Brambleton.</p>
      <div class="columns">
        <div class="col">
          <h4>Our Client Companies</h4>
          <p>Brambleton maintains a high level of discretion on both the candidate and client sides of the business. Many of the companies we recruit for are not advertising the positions elsewhere; it is critical to them that their openings remain under the radar of the marketplace, and in some cases, their existing team.</p>
          <p>What we can tell you is that we work with cutting edge clients of all sizes within our practice areas.</p>
          <p>Brambleton is a boutique firm allowing us to provide the personal attention both our clients and candidates deserve.</p>
        </div>
        <div class="col">
          <h4>Our Candidates</h4>
          <p>We place entry level candidates through mid-level professionals through to C-Level executives. Our goal is for a candidate to work with us throughout their career.</p>
          <p>Turning to us doesn't always mean making a move; in the past we have recognized and advised members of our network that it is in their best interest to stick it out at their current position for a little longer.</p>
          <p>We have the experience to recognize the appropriate next step for you, and the integrity to do what is in your best interest.</p>
        </div>
        <div class="col">
          <h4>Your Resume</h4>
          <p>When we receive your information, the first thing we do is try to understand exactly what you are looking for. We then check our current openings and consider our clients to see if we may have a match. If we think we might have something we will contact you to discuss it further. If we don't find an immediate match, we will save your information in our proprietary database. Whenever we receive a new opening, we review resumés in our database to see if we might have a match. We never sell or share the information in our database with third parties. Brambleton understands the importance of discretion, and will NEVER share your name, or your resumé, without your consent.</p>
        </div>
      </div>
    </div>
  </section>

  <section class="page page--right">
    <div class="employers">
      <span class="pill">Employers</span>
      <p class="lead">We provide the following service offerings:</p>
      <h4>Contingency Search – Direct Hire / Permanent</h4>
      <p>On a contingent basis we research, identify and introduce qualified candidates, manage the interview and selection process, provide detailed references and background information, negotiate compensation and provide valuable feedback after candidates start.</p>
      <p>Our clients are only billed for service if a candidate is successfully hired and should this candidate not remain employed beyond our 100 percent guarantee period Brambleton will find you a replacement candidate at zero cost – there's no better risk-free way to bring top talent directly into your organization.</p>
      <h4>Retained Search / Executive Search – Direct Hire / Permanent</h4>
      <p>Our Executive Search/Retained Search option provides a dedicated team of researchers, candidate developers and search consultants who commit to your specific project and timeframe. We remain in constant communication with you during the search process in order to ensure your complete satisfaction with our service.</p>
      <h4>Temporary and Contract Staffing</h4>
      <p>A direct hire is not always the best option – last-minute coverage requirements, short- and long-term projects, holiday shortages and interim demands for specific expertise are constant in the strategic staffing marketplace.</p>
      <p>With our temporary and contract staffing divisions, your project and temporary work gets done with one phone call. We do everything from interviewing, hiring and terminating employees, to communicating pay rate and benefits, distributing paychecks, computing wages and withholdings, maintaining personnel and payroll records, maintaining liability, fidelity and Workers' Compensation insurance coverage, and performing certain application procedures including completion of I-9 forms.</p>
      <h4>Temporary / Contract-to-Hire</h4>
      <p>Sometimes you want to audition potential candidates to see how they work. Other times, interim positions may become full-time jobs. Through this flexible option, both clients and temporary/contract employees have the opportunity to further explore each other and make sure they're making the right decision.</p>
    </div>
    <div class="team-photo" role="img" aria-label="Photo of a business team standing behind two professionals shaking hands"></div>
  </section>
</main>
</body>
</html>
```